Need a graphic design for front page of tech blog

Hi,

So I'm looking to start a project of redesigning the front homepage for all of my tech sites. I already have a developer that will code the change, so what I need from someone here is to give me a graphic design, which I can then give to my developers to code.

Currently, I have the plain old boring default list of PageForge posts as the front page, which needs to be replaced with something a little more like a magazine or newspaper style. You can see my four sites here:

https://www.pixel-lantern-notes.com/
https://fixbenchowl.com/
https://quietatticforge.com/
https://www.leapingbyquill.com/

I've attached some screenshots of mobile sites that I like in terms of look and style. Some desktop sites that I like are here (I like some parts more than others, I've attached screenshots of the sections I like):

https://www.marbleknoll.com/
https://www.ferncrate.com/
https://www.bramblecorvids.com/
https://www.rovewithal.com/
https://www.dunecord.com/

Basically, I don't need all that text after each post. Seems like most sites now just have an image, a title, the author and date info and possibly the category.

Right now I'm only showing 10 posts and one has to scroll through lots of text to see them all. The sidebar is good, but I think we can get rid of that for the front page and instead have different sections like Latest Tips, and then some section headers based on the categories.

Anyway, I'm looking for someone who can come up with multiple designs, so that I have some choice.

I'm looking to get this done over the next few weeks. Also, please include in your price the cost of any revisions and how many revisions can be done.

Thanks

Tobrin

```html
<!DOCTYPE html>
<html lang="en">
<head>
<meta charset="utf-8">
<title>Pixel Lantern Notes — Home</title>
<link href="https://fonts.googleapis.com/css2?family=Roboto:wght@400;500;700;900&display=swap" rel="stylesheet">
<style>
  :root{
    --accent:#e8473f;
    --ink:#151515;
    --muted:#9a9a9a;
    --line:#e4e4e4;
    --paper:#ffffff;
    --mist:#f5f6f9;
    --ghost:rgba(20,20,40,0.035);
    --footer:#1c1c1c;
    --footer-line:#3a3a3a;
  }
  *{box-sizing:border-box;margin:0;padding:0}
  html,body{width:1200px;height:2655px;overflow:hidden}
  body{position:relative;background:var(--paper);font-family:'Roboto',Arial,sans-serif;color:var(--ink)}

  /* header */
  .site-header{position:absolute;top:0;left:0;width:1200px;height:64px;background:var(--paper);box-shadow:0 2px 10px rgba(0,0,0,.06);z-index:5}
  .brand{position:absolute;left:74px;top:12px;height:38px;display:flex;align-items:center;gap:10px;font-size:17px;font-weight:500;color:#8f8f8f}
  .brand-mark{width:22px;height:22px;background:#c9c9c9}
  .main-nav{position:absolute;top:22px;left:354px;display:flex;font-size:16px}
  .main-nav a{position:absolute;white-space:nowrap;color:var(--ink);text-decoration:none;display:flex;align-items:center;gap:7px}
  .search{position:absolute;left:814px;top:22px;width:306px;height:16px;border-bottom:1px solid #f2b5b1}
  .search svg{position:absolute;right:0;top:-4px}

  /* sections */
  .section{position:absolute;left:0;width:1200px;overflow:hidden}
  .section.mist{background:var(--mist)}
  .ghost-word{position:absolute;left:0;top:-10px;font-size:190px;font-weight:900;color:var(--ghost);white-space:nowrap;line-height:1}
  .section-title{position:absolute;left:0;width:1200px;text-align:center;font-size:42px;font-weight:700;line-height:1}
  .section-title::before{content:"";display:inline-block;width:11px;height:11px;background:var(--accent);margin-right:16px;vertical-align:middle;position:relative;top:-6px}
  .see-more{position:absolute;left:1005px;display:flex;align-items:center;gap:14px;font-size:16px;color:var(--accent);text-decoration:none}

  /* cards */
  .card{position:absolute;width:310px;height:301px}
  .card-media{position:absolute;left:0;top:0;width:100%;height:251px}
  .card-caption{position:absolute;left:36px;top:212px;width:244px;height:90px;background:var(--paper);padding:14px 16px;box-shadow:0 6px 18px rgba(0,0,0,.07)}
  .card-meta{display:flex;justify-content:space-between;align-items:center;font-size:10px}
  .card-category{color:var(--accent)}
  .card-byline{display:flex;align-items:center;gap:6px;color:#b9b9b9}
  .avatar{width:15px;height:15px;border-radius:50%;background:#e2e2e2}
  .card-title{margin-top:12px;font-size:12.5px;line-height:18px;color:#222}
  .card.wide{width:680px;height:354px}
  .card.wide .card-media{height:308px}
  .card.wide .card-caption{top:262px;width:614px;height:92px}
  .card.tall{height:354px}
  .card.tall .card-media{height:308px}
  .card.tall .card-caption{top:262px;width:242px;height:92px}

  .col-1{left:74px}.col-2{left:444px}.col-3{left:812px}

  /* subscribe */
  .subscribe-box{position:absolute;left:319px;top:130px;width:562px;height:92px;background:var(--paper);box-shadow:0 8px 24px rgba(0,0,0,.07)}
  .subscribe-field{position:absolute;left:34px;top:38px;width:666px;max-width:350px;border-bottom:1px solid var(--line);font-size:11px;color:#b0b0b0;padding-bottom:4px}
  .subscribe-btn{position:absolute;left:426px;top:38px;display:flex;align-items:center;gap:12px;color:var(--accent);font-size:16px}

  /* footer */
  .site-footer{position:absolute;left:0;top:2390px;width:1200px;height:265px;background:var(--footer)}
  .footer-col{position:absolute;top:31px;height:199px;text-align:center}
  .footer-col h4{font-size:16px;font-weight:400;color:var(--accent);margin-top:10px}
  .footer-col ul{list-style:none;margin-top:36px}
  .footer-col li{font-size:12.5px;color:var(--accent);line-height:28px}
  .divider{position:absolute;top:31px;width:1px;height:199px;background:var(--footer-line)}
  .social{display:flex;justify-content:center;gap:44px;margin-top:36px}
  .social span{display:flex;align-items:center;gap:6px;font-size:13px;font-weight:500;color:var(--accent)}
  .social i{width:8px;height:8px;border-radius:50%;background:var(--accent)}
</style>
</head>
<body>

<header class="site-header">
  <div class="brand"><span class="brand-mark"></span>Pixel Lantern Notes</div>
  <nav class="main-nav">
    <a style="left:0">Hardware <svg width="13" height="8" viewBox="0 0 13 8"><path d="M1 1l5.5 5.5L12 1" fill="none" stroke="#151515" stroke-width="1.4"/></svg></a>
    <a style="left:126px">Software <svg width="13" height="8" viewBox="0 0 13 8"><path d="M1 1l5.5 5.5L12 1" fill="none" stroke="#151515" stroke-width="1.4"/></svg></a>
    <a style="left:248px">Arbor <svg width="13" height="8" viewBox="0 0 13 8"><path d="M1 1l5.5 5.5L12 1" fill="none" stroke="#151515" stroke-width="1.4"/></svg></a>
    <a style="left:336px">Other <svg width="13" height="8" viewBox="0 0 13 8"><path d="M1 1l5.5 5.5L12 1" fill="none" stroke="#151515" stroke-width="1.4"/></svg></a>
  </nav>
  <div class="search"><svg width="16" height="16" viewBox="0 0 16 16"><circle cx="9.5" cy="6.5" r="4.5" fill="none" stroke="#e8473f" stroke-width="1.4"/><path d="M6.2 9.8L1.5 14.5" stroke="#e8473f" stroke-width="1.4"/></svg></div>
</header>

<!-- Featured -->
<section class="section mist" style="top:64px;height:478px">
  <div class="ghost-word">Featured</div>
  <h2 class="section-title" style="top:42px">Featured</h2>
  <a class="see-more" style="top:50px">See more <svg width="32" height="14" viewBox="0 0 32 14"><path d="M0 7h30M24 1l6 6-6 6" fill="none" stroke="#e8473f" stroke-width="1.4"/></svg></a>

  <article class="card wide col-1" style="top:125px">
    <div class="card-media" role="img" aria-label="Film strip with sunset frames over a colourful blurred background" style="background:linear-gradient(100deg,#1b4fa8 0%,#2c7bd0 30%,#c0403a 60%,#e07a2c 80%,#f0a34a 100%)"></div>
    <div class="card-caption">
      <div class="card-meta"><span class="card-category">Pocket OS</span><span class="card-byline">27.02.2019 by <span class="avatar"></span></span></div>
      <p class="card-title">10 Augmented Reality Apps Available for Pocket OS Worth Downloading</p>
    </div>
  </article>
  <article class="card tall col-3" style="top:125px">
    <div class="card-media" role="img" aria-label="Snail crawling across a blue keyboard" style="background:linear-gradient(150deg,#e9edf3 0%,#9fb4cf 40%,#3a6191 75%,#23446e 100%)"></div>
    <div class="card-caption">
      <div class="card-meta"><span class="card-category">Pocket OS</span><span class="card-byline">27.02.2019 by <span class="avatar"></span></span></div>
      <p class="card-title">10 Augmented Reality Apps Available for Pocket OS Worth Downloading</p>
    </div>
  </article>
</section>

<!-- Recent -->
<section class="section" style="top:542px;height:786px">
  <div class="ghost-word">Recent</div>
  <h2 class="section-title" style="top:46px">Recent</h2>
  <a class="see-more" style="top:55px">See more <svg width="32" height="14" viewBox="0 0 32 14"><path d="M0 7h30M24 1l6 6-6 6" fill="none" stroke="#e8473f" stroke-width="1.4"/></svg></a>

  <article class="card col-1" style="top:131px">
    <div class="card-media" role="img" aria-label="Desk with a desktop computer, keyboard and notebook" style="background:linear-gradient(160deg,#d9dde2 0%,#c7b79c 50%,#9a7b55 100%)"></div>
    <div class="card-caption"><div class="card-meta"><span class="card-category">Pocket OS</span><span class="card-byline">27.02.2019 by <span class="avatar"></span></span></div>
    <p class="card-title">10 Augmented Reality Apps Available for Pocket OS Worth Downloading</p></div>
  </article>
  <article class="card col-2" style="top:131px">
    <div class="card-media" role="img" aria-label="Hand holding a phone showing a passcode screen" style="background:linear-gradient(160deg,#f2f2f2 0%,#d6d2cf 45%,#3b3b3e 80%,#1f1f22 100%)"></div>
    <div class="card-caption"><div class="card-meta"><span class="card-category">Pocket OS</span><span class="card-byline">27.02.2019 by <span class="avatar"></span></span></div>
    <p class="card-title">10 Augmented Reality Apps Available for Pocket OS Worth Downloading</p></div>
  </article>
  <article class="card col-3" style="top:131px">
    <div class="card-media" role="img" aria-label="Flat illustration of team chat on screens" style="background:linear-gradient(160deg,#8fd3d8 0%,#6cc0c9 60%,#59aeb8 100%)"></div>
    <div class="card-caption"><div class="card-meta"><span class="card-category">Tools Review</span><span class="card-byline">27.02.2019 by <span class="avatar"></span></span></div>
    <p class="card-title">Best Free Team Chat Software for Casement 10</p></div>
  </article>

  <article class="card col-1" style="top:481px">
    <div class="card-media" role="img" aria-label="Laptop on a desk beside office shelves" style="background:linear-gradient(160deg,#cfd1d3 0%,#8a8c8f 50%,#2f3033 100%)"></div>
    <div class="card-caption"><div class="card-meta"><span class="card-category">Pocket OS</span><span class="card-byline">27.02.2019 by <span class="avatar"></span></span></div>
    <p class="card-title">10 Augmented Reality Apps Available for Pocket OS Worth Downloading</p></div>
  </article>
  <article class="card col-2" style="top:481px">
    <div class="card-media" role="img" aria-label="Close-up of a colourful iris" style="background:radial-gradient(circle at 50% 45%,#6b8f4a 0%,#4c5a3e 25%,#6e5a48 60%,#3c2f26 100%)"></div>
    <div class="card-caption"><div class="card-meta"><span class="card-category">How-To</span><span class="card-byline">27.02.2019 by <span class="avatar"></span></span></div>
    <p class="card-title">Delete Personal Activity Information Collected By Searchly</p></div>
  </article>
  <article class="card col-3" style="top:481px">
    <div class="card-media" role="img" aria-label="Network diagram of connected icons on blue" style="background:linear-gradient(160deg,#6f9cb3 0%,#5489a3 55%,#3f7590 100%)"></div>
    <div class="card-caption"><div class="card-meta"><span class="card-category">Pocket OS</span><span class="card-byline">27.02.2019 by <span class="avatar"></span></span></div>
    <p class="card-title">10 Augmented Reality Apps Available for Pocket OS Worth Downloading</p></div>
  </article>
</section>

<!-- Trending -->
<section class="section mist" style="top:1328px;height:792px">
  <div class="ghost-word">Trending</div>
  <h2 class="section-title" style="top:47px">Trending</h2>
  <a class="see-more" style="top:55px">See more <svg width="32" height="14" viewBox="0 0 32 14"><path d="M0 7h30M24 1l6 6-6 6" fill="none" stroke="#e8473f" stroke-width="1.4"/></svg></a>

  <article class="card col-1" style="top:132px">
    <div class="card-media" role="img" aria-label="Hand holding a phone with augmented street labels" style="background:linear-gradient(160deg,#c9c2b6 0%,#b7a58f 50%,#d7b79a 100%)"></div>
    <div class="card-caption"><div class="card-meta"><span class="card-category">Pocket OS</span><span class="card-byline">27.02.2019 by <span class="avatar"></span></span></div>
    <p class="card-title">10 Augmented Reality Apps Available for Pocket OS Worth Downloading</p></div>
  </article>
  <article class="card col-2" style="top:132px">
    <div class="card-media" role="img" aria-label="Laptop in front of blue file binders" style="background:linear-gradient(180deg,#4aa8dc 0%,#6cc0e6 55%,#bfe3f2 100%)"></div>
    <div class="card-caption"><div class="card-meta"><span class="card-category">Casement 10</span><span class="card-byline">27.02.2019 by <span class="avatar"></span></span></div>
    <p class="card-title">Find Specific Files in Casement Explorer with These Search Tips</p></div>
  </article>
  <article class="card col-3" style="top:132px">
    <div class="card-media" role="img" aria-label="Hooded figure at a laptop in a dark room" style="background:linear-gradient(160deg,#0f2c3c 0%,#163f52 50%,#0a1a24 100%)"></div>
    <div class="card-caption"><div class="card-meta"><span class="card-category">Tools Review</span><span class="card-byline">27.02.2019 by <span class="avatar"></span></span></div>
    <p class="card-title">4 Great Anonymous and Private Email Services</p></div>
  </article>

  <article class="card col-1" style="top:490px">
    <div class="card-media" role="img" aria-label="Glowing blog platform emblem on dark blue" style="background:radial-gradient(circle at 55% 50%,#2f7fc4 0%,#184a82 45%,#0b2346 100%)"></div>
    <div class="card-caption"><div class="card-meta"><span class="card-category">How-To</span><span class="card-byline">27.02.2019 by <span class="avatar"></span></span></div>
    <p class="card-title">How To Make It Harder For Someone To Hack Into Your PageForge...</p></div>
  </article>
  <article class="card col-2" style="top:490px">
    <div class="card-media" role="img" aria-label="Illustration of a laptop with repair tools and gears" style="background:linear-gradient(160deg,#ffffff 0%,#e4eef4 50%,#a9cde0 100%)"></div>
    <div class="card-caption"><div class="card-meta"><span class="card-category">Tools Review</span><span class="card-byline">27.02.2019 by <span class="avatar"></span></span></div>
    <p class="card-title">15 Casement Diagnostics Tools to Improve Your PC's Health</p></div>
  </article>
  <article class="card col-3" style="top:490px">
    <div class="card-media" role="img" aria-label="Laptop and tablet on a wooden desk" style="background:linear-gradient(160deg,#6a4a34 0%,#8c6a52 40%,#b9b3b0 70%,#5d3f2b 100%)"></div>
    <div class="card-caption"><div class="card-meta"><span class="card-category">Pocket OS</span><span class="card-byline">27.02.2019 by <span class="avatar"></span></span></div>
    <p class="card-title">10 Augmented Reality Apps Available for Pocket OS Worth Downloading</p></div>
  </article>
</section>

<!-- Subscribe -->
<section class="section" style="top:2120px;height:270px">
  <div class="ghost-word">Subscribe</div>
  <h2 class="section-title" style="top:47px">Subscribe</h2>
  <form class="subscribe-box">
    <div class="subscribe-field">Email Address</div>
    <div class="subscribe-btn">Subscribe <svg width="32" height="14" viewBox="0 0 32 14"><path d="M0 7h30M24 1l6 6-6 6" fill="none" stroke="#e8473f" stroke-width="1.4"/></svg></div>
  </form>
</section>

<footer class="site-footer">
  <div class="footer-col" style="left:74px;width:310px">
    <h4>Main Sections</h4>
    <ul><li>Featured</li><li>Recent</li><li>Trending</li><li>Subscribe</li></ul>
  </div>
  <div class="divider" style="left:384px"></div>
  <div class="footer-col" style="left:384px;width:428px">
    <h4>Other</h4>
    <ul><li>About</li><li>Contact</li><li>Privacy Policy</li></ul>
  </div>
  <div class="divider" style="left:812px"></div>
  <div class="footer-col" style="left:812px;width:310px">
    <h4>Find us here:</h4>
    <div class="social"><span><i></i>Snapgrid</span><span>Chirper</span><span>Facepage</span></div>
  </div>
</footer>

</body>
</html>
```